Pet Shop Website

website will need to have the following features:
• Photo Galleries of each species (Dogs, Cats, Birds, Fish, Reptiles, Rabbits) in a light box popup
o Each species may have several different categories for example:
 Fish
• Marine fish
• Fresh water
• tropical
• Cichlid
• Information Fact sheets of each species – Downloaded as a pdf which can be either
o Care Sheets
o Training Sheets
• Members Area
o Username (Email Address) & Password login
o New signups
o Exclusive Member Deals
o Newsletter options

The front page must be very simple (for example lumavale.com.au) contain the following:
• Product of the week - which can be purchased online
o Short details
o Cost
• Pet Club Sign up picture
• Animal of the week/month
• Contact Phone Number and addresses of the stores
• A jQuery slideshow (Images could include stores, pets etc…)
The main page MUST keep simple. We do not want it cluttered.

Inner Page
The animals / reptile page will need to have:
• Short description of the species
• Photo Galleries
• A list of what is in stock and the list needs to clearly be sorted by each store (Use of Tabs maybe).
• Facts sheets / Info sheets
The type of website ideas (not the type of look that we are necessary after) is and the sort of content that we want to offer are as follows:

http://www.scalenook.com.au/
http://www.marrowdenpets.com.au/
http://www.thefurloft.com.au
http://www.critterhaven.net.au

Colour in the new website:
Blue
Red
Grey
Yellow

Original site:

http://www.pawglint.com.au
Updates

Hi Guys,

We had feedback from the client and they would like to see a few dark designs.

Thanks                                   

Reason: We would like to reopen this contest back up for a further week

Target Market(s)

Targeting animal lovers

Industry/Entity Type

Store

Requirements
Should not have
• Alter the logo in anyway

```html
<!DOCTYPE html>
<html lang="en">
<head>
<meta charset="utf-8">
<title>Pawglint – Pet Shop</title>
<link href="https://fonts.googleapis.com/css2?family=Oswald:wght@400&family=Ubuntu:wght@400;500;700&display=swap" rel="stylesheet">
<style>
:root{
  --page:#f4f4f4;
  --panel:#ffffff;
  --line:#dcdcdc;
  --nav-top:#3a4aa8;
  --nav-bottom:#26308a;
  --red:#c4121a;
  --red-dark:#9a0c12;
  --green:#8bb31c;
  --green-dark:#5f8a0c;
  --teal:#1f9e96;
  --yellow:#f6c500;
  --yellow-light:#ffd93b;
  --ink:#222;
  --muted:#8a8a8a;
  --stock:#4cb82a;
  --footer:#262626;
  --footer-bar:#2f2f2f;
  --footer-text:#8e8e8e;
}
*{box-sizing:border-box;margin:0;padding:0}
html,body{width:1123px;height:1200px;overflow:hidden}
body{background:var(--page) repeating-linear-gradient(135deg,#f7f7f7 0 2px,#f1f1f1 2px 4px);font-family:"Ubuntu",sans-serif;color:var(--ink);position:relative}
.site{position:absolute;left:103px;top:0;width:917px}
.utility{position:absolute;right:70px;top:7px;font-size:12px;color:#333;font-family:"Oswald",sans-serif;font-weight:400}
.utility span{margin:0 6px;color:#888}
.masthead{position:absolute;top:28px;left:0;width:917px;height:120px;background:linear-gradient(#f8f8f8,#e8e8e8);border:1px solid #e0e0e0;border-bottom:none;border-radius:4px 4px 0 0}
.brand{position:absolute;left:24px;top:38px;display:flex;align-items:center;gap:10px;font-size:34px;font-weight:700;color:var(--nav-bottom)}
.brand-dot{width:30px;height:30px;border-radius:50%;background:var(--yellow)}
.hotline{position:absolute;right:56px;top:40px;display:flex;align-items:center;gap:12px}
.hotline p{font-family:"Oswald",sans-serif;font-size:19px;line-height:24px;color:#444}
.mainnav{position:absolute;top:148px;left:0;width:917px;height:44px;background:linear-gradient(var(--nav-top),var(--nav-bottom));border-radius:0 0 4px 4px;display:flex}
.mainnav a{font-family:"Oswald",sans-serif;font-size:17px;color:#fff;text-decoration:none;line-height:44px;padding:0 30px 0 37px;border-right:1px solid #1d2670;box-shadow:1px 0 0 #4b5bb8}
.mainnav a:nth-child(2){padding:0 30px 0 27px}
.mainnav a:nth-child(3){padding:0 27px 0 28px}
.mainnav a:nth-child(4){border:none;box-shadow:none}
.search{position:absolute;right:8px;top:6px;width:242px;height:32px;background:#fff;border-radius:4px;border:2px solid #d8dcf0}
.search span{position:absolute;left:14px;top:8px;font-family:"Oswald",sans-serif;font-size:11px;color:#777}
.btn-go{position:absolute;right:2px;top:2px;width:44px;height:24px;background:linear-gradient(#2bb3aa,#168a83);border-radius:3px;color:#fff;font-size:13px;text-align:center;line-height:24px}
.hero{position:absolute;top:209px;left:0;width:917px;height:354px;border-radius:4px;overflow:hidden;border:1px solid #ccc}
.hero-photo{position:absolute;inset:0;background:radial-gradient(ellipse 90px 160px at 53% 55%,#d9ad63 0 96%,transparent 100%),radial-gradient(circle at 60% 40%,#c4de5a,#9cc43c 60%,#7aa82c)}
.hero-copy{position:absolute;left:38px;top:64px;width:360px;color:#fff}
.hero-copy h1{font-weight:400;font-size:28px;line-height:30px}
.hero-copy h1 strong{display:block;font-size:40px;line-height:44px;font-weight:400}
.hero-copy h1 strong em{font-style:normal;font-weight:700;color:var(--red)}
.hero-copy p{margin-top:22px;font-size:14.5px;line-height:18px}
.btn-explore{position:absolute;left:229px;top:260px;width:149px;height:38px;background:linear-gradient(#d81f22,#a80e12);border-radius:3px;color:#fff;font-size:17px;text-align:center;line-height:38px}
.dots{position:absolute;left:23px;top:335px;display:flex;gap:3px}
.dots i{width:16px;height:16px;border-radius:50%;background:#e6e2c6}
.dots i:first-child{background:#2a7fd0}
.products{position:absolute;top:580px;left:0;width:917px;height:342px;background:var(--panel);border:1px solid var(--line);border-radius:4px;overflow:hidden}
.products-head{height:52px;background:linear-gradient(var(--yellow-light),var(--yellow));font-size:18px;line-height:52px;padding-left:32px;color:#3a3000;border-bottom:1px solid #e0b200}
.cards{display:flex}
.card{width:305px;height:290px;position:relative;border-right:1px solid var(--line)}
.card:last-child{border:none}
.card h2{font-weight:400;font-size:14.5px;text-align:center;margin-top:14px}
.card-photo{position:absolute;left:16px;top:42px;width:273px;height:145px;border:1px solid #ccc;border-radius:3px}
.stock{position:absolute;left:30px;top:197px;font-size:13px;color:var(--stock)}
.price{position:absolute;right:30px;top:195px;font-size:15px;color:var(--red)}
.blurb{position:absolute;left:26px;top:214px;width:260px;font-size:11px;line-height:14px;color:var(--muted)}
.offer-title{position:absolute;left:26px;top:196px;font-size:14px;font-weight:500;color:#111}
.btn{position:absolute;top:250px;height:28px;padding:0 14px;font-size:11.5px;font-weight:500;line-height:28px;color:#fff;border-radius:3px;text-transform:uppercase}
.btn-red{background:linear-gradient(#d61b1f,var(--red-dark))}
.btn-green{background:linear-gradient(#9cc425,var(--green-dark))}
.club{position:absolute;left:16px;top:42px;width:273px;height:145px;border:1px solid #ccc;border-radius:3px;background:#fff;overflow:hidden}
.club-photo{position:absolute;left:0;top:0;width:88px;height:100%;background:linear-gradient(#f0e8e0,#c9a27a)}
.club-copy{position:absolute;left:96px;top:32px;width:168px;text-align:right}
.club-copy small{display:block;text-align:left;font-size:13px;font-weight:500;margin-left:14px}
.club-copy b{display:block;font-size:40px;line-height:40px;color:#3048a8;letter-spacing:-1.5px}
.footer{position:absolute;top:945px;left:0;width:917px;height:233px;background:var(--footer);color:var(--footer-text)}
.footer h3{position:absolute;font-weight:500;color:#fff}
.stores h3{left:21px;top:33px;font-size:20px}
.store{position:absolute;top:80px;font-size:13px;line-height:19px}
.footer .gap{margin-top:19px}
.sitemap h3{left:420px;top:38px;font-size:15px}
.sitemap ul{position:absolute;left:420px;top:80px;list-style:none;font-size:13px;line-height:19px}
.news h3{left:657px;top:38px;font-size:15px}
.news h3.follow{left:657px;top:107px;font-size:16px}
.news-field{position:absolute;left:655px;top:65px;width:243px;height:32px;background:#fff;border-radius:4px;border:2px solid #ddd}
.news-field span{position:absolute;left:14px;top:8px;font-family:"Oswald",sans-serif;font-size:11px;color:#777}
.social{position:absolute;left:657px;top:145px;display:flex;gap:10px}
.social i{width:21px;height:21px;border-radius:50%;background:#d8d8d8}
.footer-bar{position:absolute;bottom:0;left:0;width:917px;height:39px;background:var(--footer-bar);font-size:12.5px;line-height:39px;padding:0 17px;display:flex;justify-content:space-between}
.footer-bar span{margin:0 5px}
</style>
</head>
<body>
<div class="site">
  <div class="utility">Sign In<span>|</span>Contact Us</div>

  <header class="masthead">
    <div class="brand"><span class="brand-dot"></span>Pawglint</div>
    <div class="hotline">
      <svg width="38" height="46" viewBox="0 0 38 46" aria-hidden="true"><path d="M8 2c3-2 6-1 7 2l3 8c1 3 0 5-2 6l-3 2c1 6 5 13 10 17l3-2c2-1 4-1 6 1l4 6c1 2 1 5-1 6l-4 2C21 48 2 23 2 10c0-4 3-6 6-8z" fill="#333"/></svg>
      <div><p>1-800-555-0142</p><p>1-800-555-0187</p></div>
    </div>
  </header>

  <nav class="mainnav">
    <a>HOME</a><a>ABOUT US</a><a>PETS</a><a>CONTACT US</a>
    <div class="search"><span>Search Pet</span><div class="btn-go">Go</div></div>
  </nav>

  <section class="hero">
    <div class="hero-photo" role="img" aria-label="Photo of a crested songbird perched on a leafy branch against a soft green background"></div>
    <div class="hero-copy">
      <h1>Welcome to the<strong>world of <em>Pawglint</em></strong></h1>
      <p>Lorem ipsum dolor sit amet, consectetuer adipiscing elit, sed diam nonummy nibh euismod tincidunt ut laoreet dolore magna aliquam erat volutpat. Ut wisi enim ad minim veniam, quis nostrud exerci tation ullamcorper.</p>
    </div>
    <div class="btn-explore">Explore Now</div>
    <div class="dots"><i></i><i></i><i></i><i></i></div>
  </section>

  <section class="products">
    <div class="products-head">LATEST PRODUCTS</div>
    <div class="cards">
      <article class="card">
        <h2>Animal of the Month</h2>
        <div class="card-photo" role="img" aria-label="Photo of a white and ginger kitten beside red heart toys" style="background:linear-gradient(120deg,#e7e2dc,#f5f0ea 50%,#d9c8c0)"></div>
        <span class="stock">In stock</span><span class="price">$ 59.95</span>
        <p class="blurb">Lorem ipsum dolor sit amet, consectetuer adipisc elitiam nonummy nibh.</p>
        <span class="btn btn-red" style="left:26px">View Detail</span>
        <span class="btn btn-green" style="left:184px">Add to Cart</span>
      </article>
      <article class="card">
        <h2 style="margin-top:18px">Product of the Week</h2>
        <div class="card-photo" role="img" aria-label="Photo of a fluffy white puppy standing on grass" style="background:radial-gradient(ellipse at 50% 55%,#f4f4f4 0 30%,#7b8a5a 55%,#5d6b44)"></div>
        <span class="stock">In stock</span><span class="price">$ 59.95</span>
        <p class="blurb">Lorem ipsum dolor sit amet, consectetuer adipisc elitiam nonummy nibh.</p>
        <span class="btn btn-red" style="left:26px">View Detail</span>
        <span class="btn btn-green" style="left:184px">Add to Cart</span>
      </article>
      <article class="card">
        <h2 style="margin-top:18px">Pet Club Sign Up</h2>
        <div class="club">
          <div class="club-photo" role="img" aria-label="Photo of a happy beagle puppy"></div>
          <div class="club-copy"><small>LIMMITED OFFER</small><b>Join Pet<br>Club</b></div>
        </div>
        <span class="offer-title">Limmited Time Offer</span>
        <p class="blurb" style="top:215px">Join Pet club Limited time offer and win Exclusive prizes.</p>
        <span class="btn btn-red" style="left:24px">Sign Up Now</span>
      </article>
    </div>
  </section>

  <footer class="footer">
    <div class="stores">
      <h3>OUT STORES</h3>
      <div class="store" style="left:28px">Shop 4 / 220 Harbour Rd<br>WESTMERE W.A 6120<p class="gap">Phone: (08) 5550 1970<br>Fax: (08) 5550 1960</p></div>
      <div class="store" style="left:212px">Unit 3 / 18 Meadow Drive<br>FERNVALE W.A 6171<p class="gap">Phone: (08) 5550 6619<br>Fax: (08) 5550 6613</p></div>
    </div>
    <div class="sitemap">
      <h3>SITEMAP</h3>
      <ul><li>Lorem ipsum dolor sit amet</li><li>Lorem ipsum dolor sit amet</li><li>Lorem ipsum dolor sit amet</li><li>Lorem ipsum dolor sit amet</li><li>Lorem ipsum dolor sit amet</li></ul>
    </div>
    <div class="news">
      <h3>NEWS LETTER</h3>
      <div class="news-field"><span>Enter your Email Address</span><div class="btn-go">Go</div></div>
      <h3 class="follow">Follow Us</h3>
      <div class="social"><i></i><i></i><i></i></div>
    </div>
    <div class="footer-bar">
      <div>Home<span>|</span>About Us<span>|</span>Pets<span>|</span>Contact US</div>
      <div>Copyright. Pawglint. All Rights Reserved.</div>
    </div>
  </footer>
</div>
</body>
</html>
```